Design a business card & stationary for a mortgage company

We are looking for a good looking business card design for our mortgage company that includes our logo. We received a free design as part of our logo project but we don't love it. The company is called "Pinecrest Mortgage Company" so we like waves and lighthouses. The logo should be included. We have a version in both vertical and horizontal that we have provided.

Industry/Entity Type

Finance

Contact Information for Business Card

This should include our new logo file

Requirements
Must have
• 3. The details you'd like on the card - name, title, phone, email, website, address, social media handles etc.
1. Marcus Hale
Vice President
732-419-6253
Fax 888-304-2918
mhale@pinecrestmortgage.example
NMLS 47162 - Company NMLS 61290
18 Larkin Ave
Toms River, NJ 08614

```html
<!DOCTYPE html>
<html lang="en">
<head>
<meta charset="utf-8">
<title>Pinecrest Mortgage Company – Business Card</title>
<link rel="stylesheet" href="https://fonts.googleapis.com/css2?family=Jost:wght@400;500&display=swap">
<style>
  :root {
    --navy: #135a97;
    --sky: #1a8fd6;
    --icon: #9fd0f2;
    --white: #ffffff;
    --backdrop: #d9dde2;
  }
  * { margin: 0; padding: 0; box-sizing: border-box; }
  html, body { width: 1200px; height: 965px; overflow: hidden; }
  body {
    background: var(--backdrop);
    font-family: "Jost", sans-serif;
    position: relative;
  }
  .card {
    position: absolute;
    left: 250px;
    width: 700px;
    height: 400px;
    overflow: hidden;
    box-shadow: 0 6px 18px rgba(0,0,0,.18);
  }
  /* Back of card */
  .card-back { top: 62px; background: var(--navy); }
  .card-back .brand {
    position: absolute;
    right: 70px;
    top: 150px;
    text-align: right;
  }
  .brand-name {
    font-weight: 500;
    letter-spacing: 1px;
    line-height: 1.05;
    text-transform: uppercase;
  }
  .card-back .brand-name { color: var(--white); font-size: 40px; }
  .social {
    display: flex;
    gap: 14px;
    justify-content: flex-end;
    margin-top: 22px;
  }
  .social span {
    width: 30px; height: 30px;
    background: var(--white);
    border-radius: 6px;
  }
  /* Front of card */
  .card-front { top: 502px; background: var(--white); }
  .card-front .wave { position: absolute; inset: 0; width: 100%; height: 100%; }
  .card-front .brand {
    position: absolute;
    right: 40px;
    top: 40px;
    text-align: right;
  }
  .card-front .brand-name { color: var(--navy); font-size: 34px; }
  .person { position: absolute; left: 48px; top: 140px; }
  .person-name {
    color: var(--navy);
    font-size: 34px;
    font-weight: 500;
    text-transform: uppercase;
    letter-spacing: .5px;
    line-height: 1.2;
  }
  .person-title { color: var(--sky); font-size: 20px; margin-top: 2px; }
  .contact {
    position: absolute;
    left: 56px;
    bottom: 22px;
    list-style: none;
    color: var(--white);
    font-size: 16px;
    line-height: 25px;
  }
  .contact li { display: flex; align-items: center; gap: 10px; white-space: nowrap; }
  .contact svg {
    flex: none;
    width: 16px; height: 16px;
    fill: none; stroke: var(--icon); stroke-width: 1.8;
  }
  .licence {
    position: absolute;
    right: 36px;
    bottom: 40px;
    color: var(--white);
    font-size: 17px;
    line-height: 26px;
    text-align: right;
  }
</style>
</head>
<body>

<section class="card card-back">
  <div class="brand">
    <div class="brand-name">Pinecrest<br>Mortgage Company</div>
    <div class="social"><span></span><span></span></div>
  </div>
</section>

<section class="card card-front">
  <svg class="wave" viewBox="0 0 700 400" preserveAspectRatio="none" aria-hidden="true">
    <path d="M150 236 C300 214 470 206 600 150 C650 125 685 95 700 62 L700 100 C660 170 560 204 430 214 C310 222 220 228 150 236 Z" fill="var(--sky)"/>
    <path d="M0 400 L0 268 C60 240 160 234 300 230 C470 225 620 192 700 112 L700 400 Z" fill="var(--navy)"/>
  </svg>

  <div class="brand">
    <div class="brand-name">Pinecrest<br>Mortgage Company</div>
  </div>

  <div class="person">
    <div class="person-name">Marcus Hale</div>
    <div class="person-title">Vice President</div>
  </div>

  <ul class="contact">
    <li><svg viewBox="0 0 16 16"><path d="M4 2l3 3-2 2a9 9 0 0 0 4 4l2-2 3 3-2 2C7 14 2 9 2 4z"/></svg><span>732-419-6253</span></li>
    <li><svg viewBox="0 0 16 16"><rect x="2" y="6" width="12" height="8" rx="1"/><path d="M5 6V2h6v4"/></svg><span>888-304-2918</span></li>
    <li><svg viewBox="0 0 16 16"><rect x="1.5" y="3.5" width="13" height="9"/><path d="M1.5 3.5l6.5 5 6.5-5"/></svg><span>mhale@pinecrestmortgage.example</span></li>
    <li><svg viewBox="0 0 16 16"><circle cx="8" cy="8" r="6.5"/><path d="M1.5 8h13M8 1.5c-3 3.5-3 9.5 0 13M8 1.5c3 3.5 3 9.5 0 13"/></svg><span>www.pinecrestmortgage.example</span></li>
  </ul>

  <div class="licence">
    NMLS 47162 - Company NMLS 61290<br>
    18 Larkin Ave, Toms River, NJ 08614
  </div>
</section>

</body>
</html>
```